new letterhead/envelope/business card design for law firm

please see attached pdf of current letterhead, envelope and business card. I am also attaching my new logo that I would like to be used. basically, I am looking to refresh and simplify my letterhead/stationary and business card, keeping the following in mind:

overall, I am going for the following look:

-simple,
-modern,
-classy,
-professional

Target Market(s)

law firm clients

Industry/Entity Type

Law Firm

Contact Information for Business Card

see attachment

Font styles to use
Sans Serif

Requirements
Must have
• overall, I am going for the following look:
• -simple,
• -modern,
• -classy,
• -professional
Nice to have
• same as above
Should not have
• no serif fonts

```html
<!DOCTYPE html>
<html lang="en">
<head>
<meta charset="utf-8">
<title>Hollis Law – Business Card</title>
<link href="https://fonts.googleapis.com/css2?family=Exo+2:wght@400;500;600;700&display=swap" rel="stylesheet">
<style>
  :root {
    --navy: #0f3a6e;
    --green: #4aa040;
    --paper: #fafafa;
    --backdrop: #2e2e2e;
  }
  * { margin: 0; padding: 0; box-sizing: border-box; }
  html, body {
    width: 1200px; height: 700px; overflow: hidden;
    background: var(--backdrop);
    font-family: "Exo 2", sans-serif;
  }
  .card {
    position: absolute; left: 100px; top: 27px;
    width: 1000px; height: 646px;
    background: var(--paper);
    color: var(--navy);
    overflow: hidden;
  }
  .edge-band {
    position: absolute; right: 0; top: 0;
    width: 22px; height: 646px;
    background: var(--navy);
  }
  .edge-accent {
    position: absolute; right: 0; top: 0;
    width: 22px; height: 120px;
    background: var(--green);
  }
  .brand {
    position: absolute; left: 57px; top: 45px;
    display: flex; align-items: center; gap: 28px;
  }
  .brand-mark {
    width: 134px; height: 134px; border-radius: 50%;
    background: var(--navy);
  }
  .brand-name {
    font-weight: 700; font-size: 62px; letter-spacing: 1px;
    color: var(--navy);
  }
  .contact-list {
    position: absolute; left: 88px; top: 250px;
    list-style: none;
  }
  .contact-item {
    display: flex; align-items: center;
    height: 39.5px;
    font-size: 26px; font-weight: 500;
  }
  .contact-item svg { width: 30px; height: 30px; margin-right: 21px; flex: none; }
  .address {
    position: absolute; left: 88px; top: 432px;
    display: flex; align-items: center;
    font-size: 26px; font-weight: 500; line-height: 39px;
  }
  .address svg { width: 30px; height: 34px; margin-right: 21px; }
  .attorney {
    position: absolute; left: 567px; top: 522px;
  }
  .attorney-name { font-size: 30px; font-weight: 600; letter-spacing: 0.5px; }
  .attorney-licence { font-size: 24px; font-weight: 400; margin-top: 6px; }
</style>
</head>
<body>
<div class="card">
  <div class="edge-band"></div>
  <div class="edge-accent"></div>

  <div class="brand">
    <div class="brand-mark"></div>
    <div class="brand-name">HOLLIS LAW</div>
  </div>

  <ul class="contact-list">
    <li class="contact-item">
      <svg viewBox="0 0 30 30" fill="none" stroke="var(--navy)" stroke-width="1.6"><circle cx="15" cy="15" r="13"/><path d="M10 8l3 3-2 2c1 2 3 4 5 5l2-2 3 3-2 2c-5 0-11-6-11-11z"/></svg>
      Tel:&nbsp; 919.555.0142
    </li>
    <li class="contact-item">
      <svg viewBox="0 0 30 30" fill="none" stroke="var(--navy)" stroke-width="1.6"><rect x="4" y="14" width="22" height="10" rx="1"/><path d="M9 14V5h12v9M8 19h14"/></svg>
      Fax: 919.555.0187
    </li>
    <li class="contact-item">
      <svg viewBox="0 0 30 30" fill="none" stroke="var(--navy)" stroke-width="1.6"><circle cx="15" cy="15" r="12"/><ellipse cx="15" cy="15" rx="5" ry="12"/><path d="M3 15h24"/></svg>
      www.hollislawpa.com
    </li>
    <li class="contact-item">
      <svg viewBox="0 0 30 30" fill="none" stroke="var(--navy)" stroke-width="1.6"><rect x="3" y="8" width="24" height="15"/><path d="M3 8l12 9 12-9"/></svg>
      dan@hollislawpa.com
    </li>
  </ul>

  <div class="address">
    <svg viewBox="0 0 30 34" fill="none" stroke="var(--navy)" stroke-width="1.6"><circle cx="15" cy="8" r="4"/><path d="M15 12v16M4 28c0 3 22 3 22 0s-6-3-11-3-11 0-11 3z"/></svg>
    <div>2240 Willow Creek Road, Suite 410<br>Cary, NC 27513</div>
  </div>

  <div class="attorney">
    <div class="attorney-name">DANIEL R. HOLLIS, ESQ.</div>
    <div class="attorney-licence">Licensed in NC and FL</div>
  </div>
</div>
</body>
</html>
```